Creative Brief
RoveKeel
Business cards, Stationery, Power Points
Professional
Martin Quaile
Managing Director
1187 W Dorvan
Chicago, IL
info@RoveKeel.com
www.RoveKeel.com
Please put Pagebook, Chirper and Vid-Stream, Talkly symbols on the card
Please add a Talkly line with Talkly username rovekeel
Eat.Travel.Experience

```html
<!DOCTYPE html>
<html lang="en">
<head>
<meta charset="utf-8">
<title>RoveKeel Stationery</title>
<link href="https://fonts.googleapis.com/css2?family=Lato:wght@400;700;900&display=swap" rel="stylesheet">
<style>
  :root{
    --bg:#dcdcdc;
    --paper:#ffffff;
    --ink:#1f3550;
    --text:#5a5f66;
    --muted:#9aa0a6;
    --teal:#2f6b7a;
    --dark:#3a3b3d;
    --mark:#2b86c5;
    --accent:#1a6aa0;
    --rule:#c9ced3;
  }
  *{margin:0;padding:0;box-sizing:border-box}
  html,body{width:1200px;height:715px;overflow:hidden;background:var(--bg);font-family:'Lato',Arial,sans-serif;color:var(--text)}
  .canvas{position:relative;width:1200px;height:715px}
  .sheet{position:absolute;background:var(--paper);box-shadow:0 2px 6px rgba(0,0,0,.18)}
  .brand{display:flex;align-items:center;gap:5px;white-space:nowrap}
  .brand-dot{width:18px;height:18px;border-radius:50%;background:var(--mark);flex:none}
  .brand-name{font-weight:900;color:var(--ink);font-size:20px;letter-spacing:-.3px}
  .brand--light .brand-name{color:#fff}
  .tagline{font-size:8px;font-weight:700;color:var(--teal);letter-spacing:1px}
  .tagline--light{color:#fff}

  /* business cards */
  .card{top:19px;width:245px;height:144px}
  .card--contact{left:24px}
  .card--contact .brand{position:absolute;left:22px;top:20px}
  .card--contact .brand-name{font-size:16px}
  .card--contact .brand-dot{width:15px;height:15px}
  .contact-lines{position:absolute;left:22px;top:66px;font-size:6.5px;line-height:10px}
  .person{position:absolute;right:20px;top:68px;text-align:right}
  .person-name{font-size:11px;font-weight:700;color:var(--accent)}
  .person-title{font-size:6.5px;margin-top:2px}
  .card--centered{display:flex;flex-direction:column;align-items:center;justify-content:center;gap:8px}
  .card--plain{left:288px}
  .card--teal{left:557px;background:var(--teal)}
  .card--tag{left:826px}

  /* window strip */
  .strip{left:24px;top:175px;width:509px;height:72px}
  .strip .brand{position:absolute;left:150px;top:12px}
  .strip-address{position:absolute;left:18px;top:48px;font-size:6.5px;line-height:9px}

  /* envelopes */
  .envelopes{position:absolute;left:24px;top:259px}

  /* letterhead */
  .letter{left:547px;top:175px;width:322px;height:521px}
  .letter .brand{position:absolute;left:50%;transform:translateX(-50%);top:18px}
  .watermark{position:absolute;left:96px;top:110px;width:130px;height:130px;border-radius:50%;background:var(--mark);opacity:.08}
  .letter-body{position:absolute;left:30px;right:30px;top:70px;font-size:6.3px;line-height:8.6px}
  .letter-body p{margin-bottom:8px}
  .recipient{margin-bottom:12px}
  .signature{width:70px;height:22px;margin:4px 0 4px;background:linear-gradient(90deg,rgba(31,53,80,.12),rgba(31,53,80,.04));border-radius:3px}
  .footer{position:absolute;left:0;right:0;bottom:12px;text-align:center;font-size:5.5px;color:var(--muted)}

  /* fax */
  .fax{left:876px;top:175px;width:317px;height:521px}
  .fax .brand{position:absolute;left:50%;transform:translateX(-50%);top:18px}
  .fax-title{position:absolute;right:22px;top:68px;font-size:11px;font-weight:700;color:var(--dark);letter-spacing:1px}
  .fax-table{position:absolute;left:22px;right:22px;top:86px;border-collapse:collapse;font-size:6px}
  .fax-table td{border:1px solid var(--rule);height:13px;padding:0 4px}
  .fax-table .label{width:34px;background:#eef1f3;font-weight:700;color:var(--dark)}
  .fax-checks{position:absolute;left:22px;right:22px;top:150px;display:flex;justify-content:space-between;font-size:5.5px}
  .fax-checks span{display:flex;align-items:center;gap:2px}
  .fax-checks i{display:inline-block;width:6px;height:6px;border:1px solid var(--text)}
  .fax-comments{position:absolute;left:22px;top:166px;font-size:6px;font-weight:700;color:var(--dark)}
</style>
</head>
<body>
<div class="canvas">

  <div class="sheet card card--contact">
    <div class="brand"><span class="brand-dot"></span><span class="brand-name">RoveKeel</span></div>
    <div class="contact-lines">
      1187 W Dorvan<br>Chicago, IL<br>Tel: 312.555.0148<br>info@RoveKeel.com<br>www.RoveKeel.com<br>Talkly: rovekeel
    </div>
    <div class="person">
      <div class="person-name">Martin Quaile</div>
      <div class="person-title">Managing Director</div>
    </div>
  </div>

  <div class="sheet card card--centered card--plain">
    <div class="brand"><span class="brand-dot"></span><span class="brand-name">RoveKeel</span></div>
  </div>

  <div class="sheet card card--centered card--teal">
    <div class="brand brand--light"><span class="brand-dot"></span><span class="brand-name">RoveKeel</span></div>
    <div class="tagline tagline--light">Eat | Travel | Experience</div>
  </div>

  <div class="sheet card card--centered card--tag">
    <div class="brand"><span class="brand-dot"></span><span class="brand-name">RoveKeel</span></div>
    <div class="tagline">Eat | Travel | Experience</div>
  </div>

  <div class="sheet strip">
    <div class="brand"><span class="brand-dot"></span><span class="brand-name">RoveKeel</span></div>
    <div class="strip-address">1187 W Dorvan, Chicago, IL</div>
  </div>

  <svg class="envelopes" width="509" height="437" viewBox="0 0 509 437">
    <g class="envelope envelope--white">
      <rect x="0" y="0" width="509" height="138" fill="#fff"/>
      <path d="M0 0H509V18L254.5 96L0 18Z" fill="#f4f5f6" stroke="#d5d9dc"/>
      <circle cx="254.5" cy="84" r="12" fill="#2b86c5"/>
    </g>
    <g class="envelope envelope--teal">
      <rect x="0" y="148" width="509" height="138" fill="#fff"/>
      <path d="M0 148H509V166L254.5 244L0 166Z" fill="#2f6b7a"/>
      <circle cx="254.5" cy="232" r="12" fill="#2b86c5"/>
    </g>
    <g class="envelope envelope--dark">
      <rect x="0" y="297" width="509" height="140" fill="#fff"/>
      <path d="M0 297H509V315L254.5 393L0 315Z" fill="#3a3b3d"/>
      <circle cx="254.5" cy="381" r="12" fill="#2b86c5"/>
    </g>
  </svg>

  <div class="sheet letter">
    <div class="brand"><span class="brand-dot"></span><span class="brand-name">RoveKeel</span></div>
    <div class="watermark"></div>
    <div class="letter-body">
      <p class="recipient">Harbor Line Studio<br>220 Lake Street<br>Evanston, Illinois</p>
      <p>Dear Valued Partner,</p>
      <p>Thank you for choosing us to plan your coming journey. Our team has gathered fresh routes, local tables and calm places to rest along the way.</p>
      <p>Each stop is picked by people who have walked the streets themselves, tasted the food and met the hosts who will greet you on arrival.</p>
      <p>Your full plan, with times, tickets and contacts, is enclosed. Please read it at your leisure and tell us if anything should change before departure.</p>
      <p>We look forward to hearing how the trip unfolds.</p>
      <p>Warm regards,</p>
      <div class="signature" role="img" aria-label="Handwritten signature"></div>
      <p>Martin Quaile<br>Managing Director</p>
    </div>
    <div class="footer">1187 W Dorvan, Chicago, IL &nbsp;|&nbsp; info@RoveKeel.com &nbsp;|&nbsp; www.RoveKeel.com</div>
  </div>

  <div class="sheet fax">
    <div class="brand"><span class="brand-dot"></span><span class="brand-name">RoveKeel</span></div>
    <div class="fax-title">FAX</div>
    <table class="fax-table">
      <tr><td class="label">To:</td><td></td><td class="label">From:</td><td></td></tr>
      <tr><td class="label">Fax:</td><td></td><td class="label">Pages:</td><td></td></tr>
      <tr><td class="label">Phone:</td><td></td><td class="label">Date:</td><td></td></tr>
      <tr><td class="label">Re:</td><td></td><td class="label">CC:</td><td></td></tr>
    </table>
    <div class="fax-checks">
      <span><i></i>Urgent</span><span><i></i>For Review</span><span><i></i>Please Comment</span><span><i></i>Please Reply</span><span><i></i>Please Recycle</span>
    </div>
    <div class="fax-comments">Comments:</div>
    <div class="footer">1187 W Dorvan, Chicago, IL &nbsp;|&nbsp; info@RoveKeel.com &nbsp;|&nbsp; www.RoveKeel.com</div>
  </div>

</div>
</body>
</html>
```